Business Card for Orvane Parts Wholesale supplier

Hi There! I need a new business card for our company. We are specialized in selling Orvane parts, mostly we sell new LCD screens for Telvox and Slatrons. I would like to see that back in the design.

You can find the colors and logo's on our website: www.dorvak-example.nl

Industry/Entity Type

Business

Contact Information for Business Card

My Details:
Lars Vintorp

Phone: 0031612873406
E-mail: Lars@dorvak-example.nl

Slogan: "Because Quality Matters"

Font styles to use
Sans Serif

Colors

Designer to choose colors to be used in the design.

Requirements
Must have
• A Black backside with the Dorvak logo on it. The front side should be clean with only my contact details.
• But I'm also open for something really different or awesome!
Nice to have
• Remember that we are in the parts & repairing industry, So i'll be handing those business cards mainly to repair companies. Maybe you can do something with that thought :)

```html
<!DOCTYPE html>
<html lang="en">
<head>
<meta charset="utf-8">
<title>Dorvak business card</title>
<link href="https://fonts.googleapis.com/css2?family=Questrial&display=swap" rel="stylesheet">
<style>
  :root {
    --backdrop: #bcbbb8;
    --card-black: #070707;
    --card-slate: #2a2d3a;
    --accent: #f07528;
    --accent-dark: #b95419;
    --text-light: #e4e4e4;
    --text-white: #ffffff;
  }
  * { margin: 0; padding: 0; box-sizing: border-box; }
  html, body { width: 1200px; height: 1200px; overflow: hidden; }
  body {
    background: var(--backdrop);
    font-family: "Questrial", sans-serif;
    position: relative;
  }
  .card {
    position: absolute;
    box-shadow: 0 0 3px rgba(0,0,0,0.45);
  }
  .card-front {
    left: 112px; top: 152px; width: 978px; height: 395px;
    background: var(--card-slate);
  }
  .front-identity {
    position: absolute; left: 0; top: 0; width: 486px; height: 100%;
    background: var(--card-black);
  }
  .brand-mark {
    position: absolute; left: 0; width: 486px; top: 120px;
    display: flex; align-items: center; justify-content: center; gap: 14px;
    color: var(--accent); font-size: 56px; line-height: 1;
  }
  .brand-mark .brand-square {
    width: 34px; height: 34px; background: var(--accent);
  }
  .person-name {
    position: absolute; left: 0; width: 486px; top: 228px;
    text-align: center; color: var(--text-light);
    font-size: 31px; letter-spacing: 1px;
  }
  .contact-tab {
    position: absolute; left: 450px; top: 86px; width: 143px; height: 219px;
    background: var(--accent);
    border: 1px solid #f6a777;
    box-shadow: -2px 2px 3px rgba(0,0,0,0.4);
  }
  .contact-tab::before, .contact-tab::after {
    content: ""; position: absolute; left: 30px; width: 6px; height: 12px;
    background: var(--accent-dark);
  }
  .contact-tab::before { top: -12px; clip-path: polygon(0 100%, 100% 0, 100% 100%); }
  .contact-tab::after { bottom: -12px; clip-path: polygon(0 0, 100% 0, 100% 100%); }
  .contact-icon {
    position: absolute; left: 37px; width: 76px; height: 52px;
  }
  .contact-icon.phone { top: 34px; }
  .contact-icon.web { top: 136px; }
  .contact-line {
    position: absolute; left: 616px; color: var(--text-white);
    font-size: 22px; letter-spacing: 0.5px; line-height: 1;
  }
  .contact-line.phone { top: 134px; }
  .contact-line.email { top: 236px; }

  .card-back {
    left: 104px; top: 600px; width: 987px; height: 397px;
    background: var(--card-black);
    overflow: hidden;
  }
  .back-texture {
    position: absolute; inset: 0;
    background: radial-gradient(ellipse at 60% 85%, #2a2a2a 0%, #151515 35%, #0a0a0a 75%);
  }
  .back-brand {
    position: absolute; left: 0; right: 0; top: 100px;
    display: flex; align-items: center; justify-content: center; gap: 28px;
    color: var(--text-white); font-size: 118px; line-height: 1;
    letter-spacing: 4px;
  }
  .back-brand .brand-square {
    width: 92px; height: 92px; background: var(--accent);
  }
  .slogan {
    position: absolute; left: 0; right: 0; top: 248px;
    text-align: center; padding-left: 200px;
    color: var(--text-white); font-size: 25px; letter-spacing: 0.5px;
  }
</style>
</head>
<body>

  <section class="card card-front">
    <div class="front-identity">
      <div class="brand-mark"><span class="brand-square"></span><span>Dorvak</span></div>
      <p class="person-name">Lars Vintorp</p>
    </div>

    <div class="contact-tab">
      <svg class="contact-icon phone" viewBox="0 0 76 52">
        <ellipse cx="38" cy="26" rx="38" ry="26" fill="#2a2d3a"/>
        <path d="M29 15c2-1 4 0 5 2l2 4c1 2 0 3-1 4l-2 1c1 3 4 6 7 7l1-2c1-1 2-2 4-1l4 2c2 1 3 3 2 5-1 2-3 4-6 3-8-2-15-9-17-17-1-4 0-7 1-8z" fill="#ffffff"/>
      </svg>
      <svg class="contact-icon web" viewBox="0 0 76 52">
        <ellipse cx="38" cy="26" rx="38" ry="26" fill="#2a2d3a"/>
        <g fill="none" stroke="#ffffff" stroke-width="2">
          <circle cx="38" cy="26" r="14"/>
          <ellipse cx="38" cy="26" rx="6" ry="14"/>
          <line x1="38" y1="12" x2="38" y2="40"/>
          <line x1="24" y1="26" x2="52" y2="26"/>
          <line x1="26" y1="19" x2="50" y2="19"/>
          <line x1="26" y1="33" x2="50" y2="33"/>
        </g>
      </svg>
    </div>

    <p class="contact-line phone">0031612873406</p>
    <p class="contact-line email">Lars@dorvak-example.nl</p>
  </section>

  <section class="card card-back">
    <div class="back-texture" role="img" aria-label="Dark cracked-glass texture across the card"></div>
    <div class="back-brand"><span class="brand-square"></span><span>Dorvak</span></div>
    <p class="slogan">"Because Quality Matters"</p>
  </section>

</body>
</html>
```